Website for Boutique Property Consultancy in UK

We are looking to designing a website for our Property Consultancy Services that follows a minimalistic clean style that is also bold and intriguing.
The website will be based on one landing page and a link to plain circle Page and email link.

Dominant features will be the company logo or icon and colours.

Brand colours provided for guidance.

Looking to achieve a minimalistic clean style that is also bold and intriguing.

"Updated"
Page 1 - Landing Page with the Hyperlinks to Pick a Service, Training Portal and Maple Nine Portal. example landing page https://tilbrook-studio.co.uk/

Page 2 - Shows all the Services and Sectors

Target Market(s)

Occupier Clients, Tech Companies, Property Developers, Infrastructure Clients and Major Consultants

Industry/Entity Type

Construction

Coding

Coded - Design and coding required

Number of Pages Required

2 page

Font styles to use
Other font styles liked:
• Century Gothic or Futuris (Headings)

Colors
0054AA
0677BA
7BADD7
CADEEF
E8F1F8
00AB8E
00BBA5
67D7C9
C6EFE9
E9F9F6

Requirements
Must have
• Company Logo, link to enquiry and plain circle

```html
<!DOCTYPE html>
<html lang="en">
<head>
<meta charset="utf-8">
<title>Corran Hale – Property Consultancy</title>
<link rel="stylesheet" href="https://fonts.googleapis.com/css2?family=Questrial&display=swap">
<style>
  :root {
    --orange: #f26a1b;
    --green: #1ec075;
    --ink: #09042d;
    --navy: #131338;
    --mist: #e9e9eb;
    --stage: #d3d3db;
    --grey-text: #6d6d7a;
    --white: #ffffff;
  }
  * { box-sizing: border-box; margin: 0; padding: 0; }
  html, body { width: 756px; height: 1200px; overflow: hidden; background: var(--stage); }
  body { font-family: "Questrial", "Century Gothic", sans-serif; position: relative; }
  .site {
    position: absolute; left: 64px; top: 0;
    width: 940px; height: 1796px;
    transform: scale(0.6682); transform-origin: top left;
    overflow: hidden;
  }
  .abs { position: absolute; white-space: nowrap; }

  /* Hero */
  .hero { position: absolute; left: 0; top: 0; width: 940px; height: 498px; background: var(--navy); }
  .brand { left: 60px; top: 15px; font-size: 15px; color: var(--white); letter-spacing: .3px; }
  .nav { left: 236px; top: 19px; display: flex; gap: 22px; font-size: 9px; color: var(--white); }
  .hero-label { left: 60px; top: 194px; font-size: 8px; letter-spacing: 2.6px; color: var(--orange); text-transform: uppercase; }
  .hero-title { left: 59px; top: 208px; font-size: 30px; line-height: 35px; color: var(--white); font-weight: 400; }
  .hero-title .accent { color: var(--green); }
  .hero-arrow { left: 60px; top: 346px; }
  .hero-photo { left: 462px; top: 0; width: 270px; height: 498px;
    background: linear-gradient(160deg, #d9dbe0 0%, #a9acb4 35%, #4a4d58 65%, #2a2c36 100%); }
  .follow { left: 804px; top: 19px; font-size: 8.5px; color: var(--white); }
  .follow-dot { left: 857px; top: 11px; width: 27px; height: 27px; border-radius: 50%; background: var(--green); }
  .audience { width: 150px; text-align: center; font-size: 8.5px; line-height: 15px; color: var(--white); left: 767px; }
  .audience-rule { left: 797px; top: 289px; width: 143px; height: 1px; background: rgba(255,255,255,.45); }

  /* Services */
  .photo-desk { left: 0; top: 498px; width: 582px; height: 426px;
    background: radial-gradient(ellipse at 60% 55%, #8a8c95 0%, #3a3f55 45%, #181a26 100%); }
  .panel-light { left: 582px; top: 498px; width: 358px; height: 426px; background: var(--mist); }
  .section-title { font-size: 20px; line-height: 22px; font-weight: 400; }
  .service-list { list-style: none; font-size: 9.5px; }
  .service-list li { height: 21.7px; position: relative; padding-left: 11px; }
  .service-list li::before { content: ""; position: absolute; left: 0; top: 4px; width: 4px; height: 4px; border-radius: 50%; background: var(--green); }
  .service-list.warm li::before { background: var(--orange); }
  .pre { left: 654px; top: 587px; color: var(--navy); }
  .pre-list { left: 654px; top: 648px; color: var(--navy); }

  .panel-post { left: 0; top: 924px; width: 358px; height: 426px; background: var(--navy); }
  .post { left: 86px; top: 1044px; color: var(--white); }
  .post-list { left: 86px; top: 1112px; color: var(--white); }
  .panel-sector { left: 358px; top: 924px; width: 582px; height: 213px; background: var(--ink); }
  .sector { left: 478px; top: 997px; color: var(--white); }
  .sector-list { left: 478px; top: 1033px; color: var(--white); }
  .photo-house { left: 358px; top: 1137px; width: 582px; height: 213px;
    background: linear-gradient(180deg, #7f9ad0 0%, #c7b2cf 45%, #3a4468 75%, #222a47 100%); }

  /* Contact */
  .contact { left: 0; top: 1350px; width: 940px; height: 446px; background: var(--mist); }
  .contact-title { left: 92px; top: 1432px; font-size: 22px; color: var(--navy); font-weight: 400; }
  .contact-copy { left: 94px; top: 1479px; font-size: 9.4px; line-height: 17px; color: var(--grey-text); }
  .badge { left: 92px; top: 1599px; width: 56px; height: 22px; background: var(--navy); border-radius: 3px; }
  .copyright { left: 92px; top: 1642px; font-size: 7px; color: var(--grey-text); }
  .field { width: 234px; height: 17px; border-bottom: 1px solid var(--green); font-size: 9px; color: var(--navy); }
  .field.wide { width: 481px; height: 71px; }
  .send { left: 363px; top: 1677px; width: 82px; height: 32px; background: var(--navy); color: var(--white);
    font-size: 9px; display: flex; align-items: center; justify-content: center; letter-spacing: .3px; }
</style>
</head>
<body>
<main class="site">
  <section class="hero">
    <div class="abs brand">Corran Hale</div>
    <nav class="abs nav"><span>Home</span><span>Services</span><span>Contact</span></nav>
    <p class="abs hero-label">Welcome to Corran Hale</p>
    <h1 class="abs hero-title">Property <span class="accent">Consultancy</span><br>Services for Your<br>Real Estate Needs</h1>
    <svg class="abs hero-arrow" width="20" height="16" viewBox="0 0 20 16" aria-hidden="true">
      <path d="M2 3 L16 13 M16 5 L16 13 L7 13" fill="none" stroke="#f26a1b" stroke-width="1.8"/>
    </svg>
    <div class="abs hero-photo" role="img" aria-label="Photo of two consultants reviewing building plans on site"></div>
    <div class="abs follow">Follow Us:</div>
    <div class="abs follow-dot"></div>
    <p class="abs audience" style="top:211px">Tech Companies,<br>Property Developers</p>
    <div class="abs audience-rule"></div>
    <p class="abs audience" style="top:337px">Infrastructure Clients<br>and Major Consultants</p>
  </section>

  <div class="abs photo-desk" role="img" aria-label="Photo of a hand signing a contract document with a pen"></div>
  <div class="abs panel-light"></div>
  <h2 class="abs section-title pre">01 - Pre-Contract<br>Services</h2>
  <ul class="abs service-list pre-list">
    <li>Specialised MEP Cost Management</li>
    <li>Programme Cost Assurance</li>
    <li>Strategic PMO Cost Advisory</li>
    <li>Benchmarking and Market Insight</li>
    <li>Development Appraisals &amp; Cost Modelling</li>
    <li>Feasibility Studies and Cost Planning</li>
    <li>Procurement and Tendering</li>
    <li>Contractual Advice (SBC, ICX, NCS3,NCS4)</li>
    <li>Value Engineering and Lifecycle costing</li>
  </ul>

  <div class="abs panel-post"></div>
  <h2 class="abs section-title post">02 - Post-Contract<br>Services</h2>
  <ul class="abs service-list post-list">
    <li>Commercial Management</li>
    <li>Cost Governance/Assurance/Auditing</li>
    <li>Contract Administration</li>
    <li>Change Management</li>
    <li>Final Account Closeout</li>
    <li>Claims and Dispute Resolution</li>
  </ul>

  <div class="abs panel-sector"></div>
  <h2 class="abs section-title sector">03 - Sector Experience</h2>
  <ul class="abs service-list warm sector-list">
    <li>Commercial Offices; Retail; Residential; Hotels; Mixed Use; Industrial Parks</li>
    <li>Infrastructure; Metro Lines; Regional Rail; High Speed and Transit</li>
  </ul>
  <div class="abs photo-house" role="img" aria-label="Photo of a lit family house at dusk"></div>

  <section class="abs contact"></section>
  <h2 class="abs contact-title">Drop Us a Line</h2>
  <p class="abs contact-copy">We are thrilled that you stopped by and<br>hope you are finding the information you<br>are looking for. If you have any questions<br>or would like more information about our<br>products or services, we encourage you to<br>fill out our contact form</p>
  <div class="abs badge" role="img" aria-label="Professional accreditation badge"></div>
  <p class="abs copyright">© 2023 - CorranHale</p>

  <div class="abs field" style="left:362px;top:1442px">First Name*</div>
  <div class="abs field" style="left:609px;top:1442px">Last Name*</div>
  <div class="abs field" style="left:362px;top:1487px">Email Address*</div>
  <div class="abs field" style="left:609px;top:1487px">Phone Number*</div>
  <div class="abs field" style="left:362px;top:1532px">Subject</div>
  <div class="abs field" style="left:609px;top:1532px">Type of Service*</div>
  <div class="abs field wide" style="left:362px;top:1577px">Message</div>
  <div class="abs send">SEND FORM</div>
</main>
</body>
</html>
```